PeakVoyageHub

1. Can you describe what your company does?

Please find enclosed documents for your reference about our business doing.

2. Who are your target customers for the website?

Company Positioning: A comprehensive supplier of premier international sports travel and high-end event services.
Core Advantage: Exclusive international partnership resources and an Official Ticketing Assurance System.
Service Standard: One-Stop, High-Quality Service Solutions based on the "An once-in-a-lifetime experience" philosophy.

Our target customers for the website:
Mid-to-High-end Sports Enthusiasts
Corporate Clients
Sports Associations
Please kindly find enclosed for more details about our target customers, I think it's very important to make it clear to you.

3. Do you have an existing domain name / website address?

Yes, I have. I just applied for this new domain and it's totally a new website. www.peakvoyagehub.example

4. In addition to a Home Page, which other pages / sections would you like your website to have:
About Us
Contact Us , Office / Mailing Address
Sports Travel Products( Bucket Lists) : Globe Shield, Crown Quartet, Panathlia, Football, CHL, Golf, Skiing, Hiking,Galas
Reviews/ Unforgettable Moments
FAQs
Any other page / section you would like: Here is the website for your reference, www.lanejaunts.example
For each of the pages / sections you’d like to have, please provide the text (and images, if available) you would like to include.
Please recommend 2-3 templates to me, and let me know what kind of text I will provide to every web pages.

5. Which of the below are features and functionalities your website will need:
Image Gallery
Videos
Contact Form
Maps
FAQs
6. Please provide the URLs for the social media profiles you'd like to link to the website.

Do you know Quiet Blue Ledger?

Please let me know anything you need, thank you very much!

Have a good day!

Target Market(s)

Travel for the world-wide sports games and make an once-in-a-lifetime experience

Industry/Entity Type

sports and travel industry

Coding

Coded - Design and coding required

Number of Pages Required

5+ page

Requirements
Must have
• our logo
Nice to have
• On the homepage, I’d like a banner-style section to prominently showcase the latest products.

```html
<!DOCTYPE html>
<html lang="en">
<head>
<meta charset="UTF-8">
<title>Contact Us – PeakVoyageHub</title>
<link href="https://fonts.googleapis.com/css2?family=Montserrat:wght@500;600;700;800;900&family=Open+Sans:wght@400;600&display=swap" rel="stylesheet">
<style>
:root{
  --red:#e63946;
  --red-dark:#c81e2d;
  --ink:#1b1b1f;
  --text:#555a63;
  --muted:#8a8f98;
  --line:#dcdfe4;
  --night:#0e0f13;
  --night-2:#17181d;
  --white:#ffffff;
  --paper:#ffffff;
}
*{box-sizing:border-box;margin:0;padding:0}
html,body{width:714px;height:1200px;overflow:hidden}
body{font-family:"Open Sans",sans-serif;color:var(--text);background:var(--paper);position:relative}
h1,h2,h3,h4,.brand,.btn{font-family:"Montserrat",sans-serif}

/* Hero */
.hero{position:relative;height:250px;color:var(--white);text-align:center}
.hero-bg{position:absolute;inset:0;background:radial-gradient(ellipse at 50% 20%,#3c4a5c 0%,#1f2733 45%,#0b0e14 100%)}
.hero-bg::after{content:"";position:absolute;inset:0;background:linear-gradient(180deg,rgba(8,10,14,.65) 0,rgba(8,10,14,.35) 40%,rgba(8,10,14,.7) 100%)}
.topbar{position:relative;display:flex;align-items:center;height:26px;padding:0 16px;margin-top:6px;font-size:6.5px}
.brand{font-weight:800;font-size:9px;color:var(--red);letter-spacing:.3px;display:flex;align-items:center;gap:4px}
.brand .mark{width:7px;height:7px;background:var(--red);border-radius:50%}
.nav{display:flex;gap:15px;margin-left:auto;margin-right:14px;font-family:"Montserrat",sans-serif;font-weight:600}
.nav a{color:var(--white);text-decoration:none}
.lang{margin-right:12px;font-weight:600;font-family:"Montserrat",sans-serif}
.btn-book{background:var(--red);color:var(--white);font-weight:700;font-size:6.5px;padding:6px 11px;border-radius:12px}
.hero h1{position:relative;margin-top:64px;font-size:37px;font-weight:900;letter-spacing:1px}
.hero p{position:relative;margin-top:12px;font-size:10px}

/* Intro */
.intro{text-align:center;padding-top:62px}
.intro h2{font-size:25px;font-weight:800;color:var(--ink);letter-spacing:.5px}
.intro .bar{width:52px;height:3px;background:var(--red);margin:8px auto 0}
.intro p{margin-top:13px;font-size:8.5px;color:var(--muted)}

/* Cards */
.cards{display:flex;gap:28px;padding:0 34px 0 52px;margin-top:48px}
.card{background:var(--white);border-radius:8px;box-shadow:0 4px 18px rgba(0,0,0,.09);padding:20px 18px}
.card-info{width:294px;height:460px}
.card-form{width:306px;height:460px}
.card h3{font-size:15px;font-weight:700;color:var(--ink);line-height:1.22}
.feature{display:flex;gap:12px;margin-top:20px}
.feature .ico{flex:0 0 30px;height:30px;border-radius:50%;background:var(--red);display:flex;align-items:center;justify-content:center}
.feature h4{font-size:10px;font-weight:700;color:var(--ink);margin-top:2px}
.feature p{font-size:6.8px;line-height:1.5;margin-top:4px}
.stadium{margin-top:26px;height:120px;border-radius:6px;background:linear-gradient(180deg,#1f2a44 0%,#3c4f78 35%,#4f7a3a 62%,#2f5a27 100%)}

.form{margin-top:14px}
.row{display:flex;gap:12px}
.field{margin-bottom:11px;flex:1}
.field label{display:block;font-size:7px;font-weight:600;color:var(--ink);margin-bottom:5px}
.input{height:21px;border:1px solid var(--line);border-radius:3px;font-size:6.5px;padding:6px 7px;color:var(--ink)}
.input.active{border-color:var(--red);display:flex;justify-content:space-between}
.textarea{height:62px}
.btn-send{margin-top:4px;height:25px;border-radius:13px;background:linear-gradient(90deg,var(--red),#ef5a5a);color:var(--white);font-size:7px;font-weight:700;display:flex;align-items:center;justify-content:center;gap:5px;letter-spacing:.5px}

/* Footer */
.footer{position:absolute;left:0;right:0;top:957px;bottom:0;background:var(--night);color:#b8bcc4}
.foot-cols{display:flex;padding:27px 30px 0 30px;gap:22px}
.col{flex:1}
.col h4{font-size:11px;font-weight:800;color:var(--red);letter-spacing:.3px}
.col .rule{width:30px;height:2px;background:var(--red);margin:5px 0 11px}
.col p{font-size:6.5px;line-height:1.55}
.col ul{list-style:none;font-size:6.8px}
.col li{margin-bottom:7px;display:flex;align-items:center;gap:5px}
.col li::before{content:"›";color:var(--red);font-weight:700}
.col.contact li::before{content:none}
.dot{width:7px;height:7px;border-radius:50%;background:var(--red);flex:0 0 7px}
.socials{display:flex;gap:8px;margin-top:14px}
.socials span{width:19px;height:19px;border-radius:50%;background:#262830}
.foot-bottom{position:absolute;left:30px;right:30px;bottom:0;height:36px;border-top:1px solid #25272e;text-align:center;font-size:6px;line-height:36px;color:#8a8f98}
.to-top{position:absolute;right:13px;bottom:22px;width:18px;height:18px;border-radius:50%;background:var(--red);display:flex;align-items:center;justify-content:center}
</style>
</head>
<body>

<header class="hero">
  <div class="hero-bg" role="img" aria-label="Floodlit stadium crowd at night"></div>
  <div class="topbar">
    <div class="brand"><span class="mark"></span>PeakVoyageHub</div>
    <nav class="nav">
      <a href="#">Home</a><a href="#">Featured Sports ▾</a><a href="#">Packages &amp; Services</a><a href="#">About Us</a><a href="#">Contact Us</a>
    </nav>
    <span class="lang">English ▾</span>
    <span class="btn btn-book">BOOK NOW</span>
  </div>
  <h1>CONTACT US</h1>
  <p>Get in touch to start planning your premium sports travel experience</p>
</header>

<section class="intro">
  <h2>CONTACT US</h2>
  <div class="bar"></div>
  <p>Get in touch to start planning your premium sports travel experience</p>
</section>

<section class="cards">
  <article class="card card-info">
    <h3>Your Ultimate Sports Travel Experience</h3>
    <div class="feature">
      <div class="ico"><svg width="14" height="14" viewBox="0 0 24 24" fill="none" stroke="#fff" stroke-width="2.4"><path d="M7 4h10v5a5 5 0 0 1-10 0z"/><path d="M12 14v4M8 20h8"/></svg></div>
      <div><h4>Major Sporting Events</h4><p>Experience the thrill of Globe Shield finals, Panathlia Games, Grand Final and more with premium seating and curated packages.</p></div>
    </div>
    <div class="feature">
      <div class="ico"><svg width="14" height="14" viewBox="0 0 24 24" fill="#fff"><path d="M12 3l2.7 5.6 6.1.9-4.4 4.3 1 6.1L12 17l-5.4 2.9 1-6.1L3.2 9.5l6.1-.9z"/></svg></div>
      <div><h4>VIP Experiences</h4><p>Enjoy behind-the-scenes access, meet-and-greets with athletes, and luxury accommodations at world-class venues.</p></div>
    </div>
    <div class="feature">
      <div class="ico"><svg width="14" height="14" viewBox="0 0 24 24" fill="none" stroke="#fff" stroke-width="2.2"><circle cx="12" cy="12" r="9"/><path d="M3 12h18M12 3c3 3 3 15 0 18M12 3c-3 3-3 15 0 18"/></svg></div>
      <div><h4>Global Destinations</h4><p>From Crown Quartet tennis to Globe Shield football, we provide seamless travel experiences to the world's top sporting destinations.</p></div>
    </div>
    <div class="stadium" role="img" aria-label="Packed stadium with green pitch under lights"></div>
  </article>

  <article class="card card-form">
    <h3>Send Us A Message</h3>
    <div class="form">
      <div class="row">
        <div class="field"><label>First Name</label><div class="input"></div></div>
        <div class="field"><label>Last Name</label><div class="input"></div></div>
      </div>
      <div class="field"><label>Email Address</label><div class="input"></div></div>
      <div class="field"><label>Phone Number</label><div class="input"></div></div>
      <div class="field"><label>Sports Interest</label><div class="input active"><span>Select your interest</span><span>▾</span></div></div>
      <div class="field"><label>Subject</label><div class="input"></div></div>
      <div class="field"><label>Message</label><div class="input textarea"></div></div>
      <div class="btn btn-send">SEND MESSAGE <svg width="8" height="8" viewBox="0 0 24 24" fill="#fff"><path d="M2 21l21-9L2 3v7l15 2-15 2z"/></svg></div>
    </div>
  </article>
</section>

<footer class="footer">
  <div class="foot-cols">
    <div class="col">
      <h4>PEAKVOYAGEHUB</h4><div class="rule"></div>
      <p>Premier international sports travel and high-end event services delivering once-in-a-lifetime experiences since 2014. Your trusted partner for exclusive access to the world's most prestigious sporting events.</p>
      <div class="socials"><span></span><span></span><span></span><span></span><span></span></div>
    </div>
    <div class="col">
      <h4>QUICK LINKS</h4><div class="rule"></div>
      <ul><li>Home</li><li>Featured Sports</li><li>Packages &amp; Service</li><li>About Us</li><li>Contact Us</li></ul>
    </div>
    <div class="col">
      <h4>SPORTS EVENTS</h4><div class="rule"></div>
      <ul><li>Globe Shield</li><li>Crown Quartet Tennis</li><li>Panathlia</li><li>CHL Basketball</li><li>Golf Majors</li></ul>
    </div>
    <div class="col contact">
      <h4>CONTACT US</h4><div class="rule"></div>
      <ul>
        <li><span class="dot"></span>48 Stadium Row, Harbor City</li>
        <li><span class="dot"></span>+1 (555) 014-2298</li>
        <li><span class="dot"></span>info@peakvoyagehub.example</li>
        <li><span class="dot"></span>Mon-Fri: 9am-6pm EST</li>
      </ul>
    </div>
  </div>
  <div class="foot-bottom">© 2025 PeakVoyageHub. All rights reserved. | Premium Sports Travel Experiences | Established 2014</div>
  <div class="to-top"><svg width="8" height="8" viewBox="0 0 24 24" fill="none" stroke="#fff" stroke-width="3"><path d="M5 15l7-7 7 7"/></svg></div>
</footer>

</body>
</html>
```